依頼詳細
当院がこの度4月より、木曜診療・駐車場提携・CT導入をしたため、そのお知らせのチラシを作成いただきたいです。(A4裏表)
ラフ・素材等はございます。HP(http://mk-dental.net/)取っていただいても構いません。

※発送はポミネオ様で行う予定です。(https://pomineo.com/directmail/large-sized-postcard/
※まず表面案だけで構いませんのでお出しいただけますと幸いです。その後当選の方が決まり次第裏面もお願いしようと思います。
記載項目
添付ラフ通り
サイズ
A4
ページ数
両面
希望イメージ
シンプル 複雑
単色 カラフル
暗い 明るい
日常 高級
遊び心 厳粛
未来的 伝統的
女性的 男性的
希望する色
緑系
納品ファイル
• イラストレーター形式 (.ai)
• PNG形式 (.png)
補足説明
ポミネオのDM(https://pomineo.com/directmail/large-sized-postcard/)で患者様に発送するため、ポミネオの規定で作成願えますでしょうか。
■ 選んだ理由

全体的なデザインバランスが良かったため

■ 提案者全員のお礼・コメント

この度はご参加いただきまして誠に有難うございました!
今後とも宜しくお願いいたします。

```html
<!DOCTYPE html>
<html lang="ja">
<head>
<meta charset="utf-8">
<title>松川町ファミリー歯科 お知らせ</title>
<link href="https://fonts.googleapis.com/css2?family=M+PLUS+Rounded+1c:wght@500;700;800&family=Noto+Sans+JP:wght@400;700&display=swap" rel="stylesheet">
<style>
:root{
  --green:#5cb531;
  --green-dark:#2f8a1e;
  --green-pale:#e6f3d8;
  --pink:#e8407a;
  --pink-pale:#fbe1ea;
  --ink:#333;
  --white:#fff;
}
*{box-sizing:border-box;margin:0;padding:0}
html,body{width:849px;height:1200px;overflow:hidden;background:var(--white)}
body{font-family:"Noto Sans JP",sans-serif;color:var(--ink)}
.sheet{position:relative;width:849px;height:1200px}
.address-space{position:absolute;top:0;left:0;width:849px;height:440px;display:flex;justify-content:center;padding-top:95px;font-size:26px;color:#444;letter-spacing:2px}
.notice{position:absolute;top:440px;left:0;width:849px;height:580px;background:var(--green)}
.headline{position:absolute;top:20px;left:0;width:100%;text-align:center;font-family:"M PLUS Rounded 1c",sans-serif;font-weight:800;font-size:30px;color:var(--white);letter-spacing:1px}
.panel{position:absolute;top:84px;width:376px;height:482px;background:var(--white);border-radius:14px}
.panel--hours{left:34px}
.panel--parking{left:439px}
.badge{position:absolute;top:-24px;left:14px;background:var(--pink);color:var(--white);font-family:"M PLUS Rounded 1c",sans-serif;font-weight:800;font-size:21px;padding:10px 16px;border-radius:10px;transform:rotate(-5deg)}
.bubble{position:absolute;top:-34px;right:18px;width:104px;height:104px;border-radius:50%;background:var(--pink);color:var(--white);font-family:"M PLUS Rounded 1c",sans-serif;font-weight:800;font-size:18px;line-height:1.3;display:flex;align-items:center;justify-content:center;text-align:center}
.panel-title{font-family:"M PLUS Rounded 1c",sans-serif;font-weight:800;color:var(--green-dark);font-size:33px;line-height:1.3;text-align:center}
.panel--hours .panel-title{margin-top:44px;padding-left:30px}
.panel--parking .panel-title{margin-top:38px;padding-right:70px}
.hours-label{font-size:13px;margin:12px 0 4px 22px}
.hours-table{margin-left:22px;border-collapse:collapse;font-size:12px;width:300px}
.hours-table th,.hours-table td{border:1px solid #bbb;height:26px;text-align:center}
.hours-table thead th{background:var(--green-pale);font-weight:700}
.hours-table .time{width:78px;font-weight:400}
.mark{color:var(--green);font-size:14px}
.closed{color:#999}
.new .thu{background:var(--pink-pale);color:var(--pink)}
.closed-days{font-size:11px;margin:5px 0 0 22px}
.arrow{display:block;margin:6px 0 0 150px}
.mascot{position:absolute;right:12px;top:210px;width:56px;height:66px;border-radius:24px;background:var(--green-pale)}
.map{position:absolute;top:132px;left:20px;width:336px;height:236px;background:linear-gradient(#f4f4f4,#e9efe4);border:1px solid #ddd;border-radius:6px}
.free{position:absolute;top:386px;left:0;width:100%;text-align:center;font-family:"M PLUS Rounded 1c",sans-serif;font-weight:800;font-size:38px;color:var(--green-dark)}
.free-note{position:absolute;top:438px;left:0;width:100%;text-align:center;font-size:12px;color:#555}
.footer{position:absolute;top:1020px;left:0;width:849px;height:180px}
.services{position:absolute;top:14px;left:24px;width:440px;font-size:11px;color:#555;line-height:1.6}
.clinic{position:absolute;top:62px;left:24px;display:flex;align-items:center;gap:12px}
.clinic-mark{width:46px;height:46px;border-radius:50%;background:var(--green)}
.clinic-name{font-family:"M PLUS Rounded 1c",sans-serif;font-weight:800;font-size:36px;color:var(--green-dark)}
.clinic-en{position:absolute;top:116px;left:82px;font-size:11px;letter-spacing:1px;color:var(--green-dark)}
.access{position:absolute;top:44px;right:24px;text-align:right}
.station{font-weight:700;font-size:17px;color:var(--green-dark)}
.tel{font-family:"M PLUS Rounded 1c",sans-serif;font-weight:800;font-size:34px;color:var(--green-dark);display:flex;align-items:center;gap:6px;justify-content:flex-end}
.tel small{font-size:18px}
.address{font-size:10px;color:#555;line-height:1.5}
.url-band{position:absolute;bottom:0;left:0;width:100%;height:26px;background:var(--green);color:var(--white);font-weight:700;font-size:15px;text-align:center;line-height:26px;letter-spacing:1px}
</style>
</head>
<body>
<div class="sheet">
  <section class="address-space">宛名スペース</section>

  <section class="notice">
    <h1 class="headline">松川町ファミリー歯科が更に便利に!</h1>

    <article class="panel panel--hours">
      <div class="badge">4月1日より</div>
      <h2 class="panel-title">木曜日の診療を<br>開始します</h2>
      <div class="mascot" role="img" aria-label="歯のキャラクターのイラスト"></div>

      <p class="hours-label">●今までの診療時間</p>
      <table class="hours-table">
        <thead><tr><th class="time"></th><th>月</th><th>火</th><th>水</th><th>木</th><th>金</th><th>土</th></tr></thead>
        <tbody>
          <tr><th class="time">10:00〜13:00</th><td class="mark">●</td><td class="mark">●</td><td class="mark">●</td><td class="closed">休</td><td class="mark">●</td><td class="mark">●</td></tr>
          <tr><th class="time">14:30〜20:00</th><td class="mark">●</td><td class="mark">●</td><td class="mark">●</td><td class="closed">休</td><td class="mark">●</td><td class="mark">●</td></tr>
        </tbody>
      </table>
      <p class="closed-days">休診日：木曜日・日曜日・祝日</p>

      <svg class="arrow" width="60" height="26" viewBox="0 0 60 26"><path d="M0 0H60L30 26Z" fill="var(--pink)"/></svg>

      <p class="hours-label">●4月1日からの診療時間</p>
      <table class="hours-table new">
        <thead><tr><th class="time"></th><th>月</th><th>火</th><th>水</th><th class="thu">木</th><th>金</th><th>土</th></tr></thead>
        <tbody>
          <tr><th class="time">10:00〜13:00</th><td class="mark">●</td><td class="mark">●</td><td class="mark">●</td><td class="mark thu">●</td><td class="mark">●</td><td class="mark">●</td></tr>
          <tr><th class="time">14:30〜20:00</th><td class="mark">●</td><td class="mark">●</td><td class="mark">●</td><td class="mark thu">●</td><td class="mark">●</td><td class="mark">●</td></tr>
        </tbody>
      </table>
      <p class="closed-days">休診日：日曜日・祝日</p>
    </article>

    <article class="panel panel--parking">
      <div class="bubble">ご来院が<br>より簡単に!</div>
      <h2 class="panel-title">駐車場サービス<br>のご案内</h2>
      <div class="map" role="img" aria-label="医院周辺の提携駐車場の位置を示す地図"></div>
      <p class="free">40〜60分無料</p>
      <p class="free-note">※駐車場により異なります</p>
    </article>
  </section>

  <footer class="footer">
    <p class="services">一般歯科・小児歯科・審美歯科・予防歯科・入れ歯・インプラント</p>
    <div class="clinic"><span class="clinic-mark"></span><span class="clinic-name">松川町ファミリー歯科</span></div>
    <p class="clin-en clinic-en">MATSUKAWACHO FAMILY DENTAL CLINIC</p>
    <div class="access">
      <p class="station">緑ヶ丘線「松川町」駅徒歩1分</p>
      <p class="tel">
        <svg width="26" height="26" viewBox="0 0 24 24"><path d="M6.6 10.8a15 15 0 006.6 6.6l2.2-2.2a1 1 0 011-.25 11.4 11.4 0 003.6.6 1 1 0 011 1V20a1 1 0 01-1 1A17 17 0 013 4a1 1 0 011-1h3.5a1 1 0 011 1c0 1.25.2 2.45.6 3.6a1 1 0 01-.25 1z" fill="var(--green-dark)"/></svg>
        <small>TEL.</small>06-6000-4812
      </p>
      <p class="address">ご予約・ご相談はお気軽にお電話ください<br>〒500-0000 大阪市松川区緑ヶ丘1丁目2-3</p>
    </div>
    <div class="url-band">mk-dental.net</div>
  </footer>
</div>
</body>
</html>
```